Super Greens Label for Supplement Bottle

We want to design a front label for a health supplement bottle. The product is called Meadow Twist Chews™. This will be a new product so there is no current website for the product. The focus is on supergreens that taste great and deliver support for energy, digestion, and immune defense.
We want it to be modern, vibrant and appealing.
Bottle size: standard size supplement CLEAR bottle size, with white child resistant cap and the label panel dimensions are 3” x 7”. The label should be primarily white and green, with a touch of red; (see color palettes)/it can also ONLY be white and green. See samples attached.
We are only focused on the front of the bottle design, not on the back, but leave space for the supplement panel and other text on the back.
So the text for the front of the bottle is:
RT Balden's
Meadow Twist Chews™
Super Greens Blend for:
Energy, Digestion, and Immune Support*
60 Gummies | Dietary Supplement
Raspberry Flavor Gummies
Off to side of the label:
Non-GMO
Vegan Friendly
Plant-Based
Gelatin Free
Colors
Designer to choose colors to be used in the design.

```html
<!DOCTYPE html>
<html lang="en">
<head>
<meta charset="UTF-8">
<title>RT Balden's Meadow Twist Chews – Bottle Label</title>
<link href="https://fonts.googleapis.com/css2?family=Poppins:wght@400;500;600;700;800&display=swap" rel="stylesheet">
<style>
  :root {
    --green: #0c744a;
    --green-front: #0f7a4d;
    --white: #ffffff;
    --berry: #c8323e;
    --berry-light: #e0606a;
  }
  * { box-sizing: border-box; margin: 0; padding: 0; }
  html, body {
    width: 1200px; height: 1200px; overflow: hidden;
    background: var(--white);
    font-family: 'Poppins', sans-serif;
  }
  .canvas { position: relative; width: 1200px; height: 1200px; }
  .panel {
    position: absolute; top: 360px; height: 487px;
    background: var(--green);
  }
  .panel-left { left: 60px; width: 347px; }
  .panel-right { left: 800px; width: 347px; }
  .panel-front {
    left: 422px; width: 363px;
    background: var(--green-front);
    color: var(--white);
  }
  .brand {
    position: absolute; top: 88px; left: 0; width: 100%;
    text-align: center;
    font-weight: 500; font-size: 27px; letter-spacing: 1px;
  }
  .brand-dot {
    display: block; width: 14px; height: 14px; border-radius: 50%;
    background: var(--white); margin: 0 auto 8px;
  }
  .product-name {
    position: absolute; top: 152px; left: 28px; width: 311px;
    font-weight: 700; line-height: 1.05; letter-spacing: -0.5px;
  }
  .product-name .line { display: block; white-space: nowrap; }
  .product-name .line-1 { font-size: 43px; }
  .product-name .line-2 { font-size: 62px; letter-spacing: 0.5px; }
  .product-name sup { font-size: 16px; vertical-align: top; position: relative; top: 8px; }
  .benefits {
    position: absolute; top: 294px; left: 28px; width: 311px; height: 23px;
    background: var(--white); color: var(--green);
    font-weight: 600; font-size: 12.5px;
    display: flex; align-items: center; justify-content: center;
    white-space: nowrap;
  }
  .claims {
    position: absolute; top: 334px; left: 0; width: 100%;
    list-style: none; text-align: center;
    font-size: 10.5px; font-weight: 400;
  }
  .claims li { height: 21px; line-height: 14px; position: relative; }
  .claims li:not(:last-child)::after {
    content: ""; position: absolute; left: 50%; bottom: 5px;
    width: 56px; height: 2px; margin-left: -28px;
    background: var(--white); border-radius: 1px;
  }
  .count {
    position: absolute; left: 28px; top: 403px;
    line-height: 1;
  }
  .count-number { display: block; font-size: 30px; font-weight: 500; }
  .count-unit { display: block; font-size: 6.5px; margin-top: 1px; }
  .count-type { display: block; font-size: 10.5px; margin-top: 6px; letter-spacing: 0.2px; }
  .flavor-badge { position: absolute; left: 291px; top: 403px; width: 50px; height: 50px; }
</style>
</head>
<body>
<div class="canvas">
  <div class="panel panel-left" aria-label="Back label space for supplement facts"></div>

  <section class="panel panel-front">
    <div class="brand"><span class="brand-dot"></span>RT BALDEN'S</div>

    <h1 class="product-name">
      <span class="line line-1">Meadow Twist</span>
      <span class="line line-2">Chews<sup>™</sup></span>
    </h1>

    <p class="benefits">Energy, Digestion, and Immune Support*</p>

    <ul class="claims">
      <li>non-gmo</li>
      <li>vegan friendly</li>
      <li>plant-based</li>
      <li>gelatin free</li>
    </ul>

    <div class="count">
      <span class="count-number">60</span>
      <span class="count-unit">Gummies</span>
      <span class="count-type">Dietary Supplement</span>
    </div>

    <svg class="flavor-badge" viewBox="0 0 50 50">
      <defs>
        <path id="badge-arc" d="M25,25 m-20,0 a20,20 0 1,1 40,0 a20,20 0 1,1 -40,0"/>
      </defs>
      <circle cx="25" cy="25" r="24" fill="var(--white)"/>
      <text font-family="Poppins, sans-serif" font-size="5.4" fill="var(--green)">
        <textPath href="#badge-arc" startOffset="2%">Raspberry Flavor Gummies •</textPath>
      </text>
      <circle cx="25" cy="25" r="12" fill="var(--berry)" role="img" aria-label="Raspberries illustration"/>
    </svg>
  </section>

  <div class="panel panel-right" aria-label="Back label space for directions and warnings"></div>
</div>
</body>
</html>
```